Fundraising Gala Marketing Materials
You’re Generosity. Our Passion. Saving Lives.
Lanterns & Linden provides life-prolonging medication and support to the more than 20 million children in Africa infected or orphaned by HIV/AIDS by raising money and awareness through local events, volunteer opportunities, and online donations.
As a cloud-based nonprofit 501(c) (3) corporation, Lanterns & Linden’s programs are highly efficient and fully audited to ensure all funds are maximized to benefit on-the-ground healthcare supplies and programs.
Founded in 2004, the organization has raised hundreds of thousands of dollars, which at only $50 per month per child, which makes an impact.
What we Need | The Required Items:

Repeat graphical design across all 4 items.

1. Poster Design - Charity Fundraising Gala (poster A5)
2. Save the Date Post Card - Charity Fundraising Gala (post card just front)
3. Thank You Post Card – Charity Fundraising Gala (postcard front and back)
4. Ticket Coupons - Charity Fundraising Gala (bookmarks front and back)

The design and theme across all items should be the same. We have examples from last years to use as templates for layout, working and sizes.

What we are doing and why we need these items | Every year we host a formal gala for 200 guest – sit down 4 course plated full service event. Last year it was held at a 5 star hotel. This year it will be held a high end winery in the Seattle area. The night includes a cocktail hours, silent auction live auction, emotional speakers, live music, and dancing at the end of the night. All the wine you can drink and 4 courses for only $110. We have a number of fundraising events to raise money for HIV orphans in Africa. We aim to raise $120,000...

Attached are posters from the last year – please see for examples, but feel free to suggest something different

Main Design Work | We will basically have the same information and picture on all four items, just formatted differently.

Name of Event “Baobab Evening” We have attached some picture to give you sense of what we want. A heart and map of Africa combined. If possible work the HIV Red Ribbon into the design. Take a look at the design from last year and now come up with new Africa/Heart theme. See wording below for each.

Sizing | Format
Poster Design - Charity Fundraising Gala
We will use Quillpress Printing: http://quillpressprinting.example/
Size| A5
Resolution |300dpi
File Types | PDF

Save the Date Post Card - Charity Fundraising Gala
We will use Swiftmark prints: http://www.swiftmarkprints.example/upload/pc?new=1
Bleed Size | 4.25" x 6.25"
Trim Size | 4" x 6"
Safe Zone |3.875" x 5.875"
Resolution |300dpi
Color | for optimal printing, Swiftmark Prints recommends uploading your files in CMYK.
File Types | you may upload a number of different file types: TIF, PDF, JPG, EPS, PNG and AI (Version 8 or lower).
File Size | Total size of all your files should not exceed 100 MB
Download template from site above.

Thank You Post Card – Charity Fundraising Gala
Same as Save the Date Post Card

Ticket Coupons - Charity Fundraising Gala
http://www.swiftmarkprints.example/upload/pc2x6?new=1
Bleed Size | 2.127" x 6.127"
Trim Size | 2" x 6"
Safe Zone | 1.875" x 5.875"
Resolution | 300dpi

Text Required:
You are invited
October 18th 2014
Calder Ridge Winery
Baobab Evening
Graphic
Lanterns and Linden logo
Live entertainment, auctions, and fine wines, all to benefit Orphans in Africa.

Lanterns & Linden logo
The Logo of Calder Ridge (last year was Brackwell)
Text to example the time, date, cost and dress code:
October 18th 2014
6:30 PM
$110
4 courses
Bottomless wine from Calder Ridge

This thank you post card has a front and a back.

Front | Just Baobab Evening picture and the words Thank You.

Back| Left Side panel of Post Card:

“Your Generosity. Our Passion. Saving Lives.”

We were raised

Thank you for helping us break records this year! Your contribution is an important part of our efforts to help AIDS Positive Orphans in Africa.

Thank You!

(note we need to leave a blank space after we raided.. we will fill this value in with hand written note)
On the right side leave space for stamp and address.

See example from 2013 for front and back. Use similar format and update Tree with “Baobab Evening”. Ensure SIZE is correct believe 2013 size was too small.
Lanterns & Linden logo
October 18th 2014
$110
Calder Ridge Winery
Baobab Evening Graphic

Thank You for Helping Orphans in Africa

                                       Please send me questions and we can work on this in interactive way.

Target Market(s)

high end, folks that can donate $500 at the vent. Will be held in fancy winery

Industry/Entity Type

Healthcare

Font styles to use
Sans Serif

Colors
ec2027

Requirements
Must have
• Baobab Evening, event details, AIDS Ribbon

```html
<!DOCTYPE html>
<html lang="en">
<head>
<meta charset="utf-8">
<title>Baobab Evening – Gala Materials</title>
<link href="https://fonts.googleapis.com/css2?family=Oswald:wght@400;600;700&family=Arimo:wght@400;700&family=Open+Sans:wght@300;400&display=swap" rel="stylesheet">
<style>
:root{
  --board:#000;
  --paper:#fff;
  --paper-soft:#f4f5f3;
  --sun-top:#f7a21b;
  --sun-mid:#f26a1f;
  --sun-low:#e0341f;
  --ribbon:#ec2027;
  --brand:#e8461e;
  --map-deep:#b8161c;
  --map-warm:#f0591f;
  --ink:#111;
  --ink-soft:#333;
  --sponsor:#6d7a70;
}
*{box-sizing:border-box;margin:0;padding:0}
html,body{width:1200px;height:730px;overflow:hidden;background:var(--board)}
.board{position:relative;width:1200px;height:730px;background:var(--board);font-family:"Arimo",Arial,sans-serif}
.piece{position:absolute;overflow:hidden}
.sunset{background:linear-gradient(180deg,var(--sun-top) 0%,var(--sun-mid) 45%,var(--sun-low) 100%)}
.artwork{position:absolute;border-radius:40% 45% 35% 50%;background:radial-gradient(circle at 50% 45%,var(--sun-top) 0 14%,var(--map-warm) 26%,var(--map-deep) 70%,rgba(184,22,28,0) 72%)}
.ribbon-mark{position:absolute;background:var(--ribbon);border-radius:3px}
.headline{font-family:"Oswald",Impact,sans-serif;font-weight:700;color:var(--ink);line-height:1;text-transform:uppercase;white-space:nowrap}

/* Thank-you front */
.thanks-front{left:33px;top:83px;width:369px;height:250px;background:var(--paper)}
.thanks-front .face{position:absolute;left:12px;top:12px;width:345px;height:227px}
.thanks-front .title{position:absolute;left:156px;top:24px;font-size:21px}
.thanks-front .sub{position:absolute;left:156px;top:43px;font-size:14px}
.thanks-front .tag{position:absolute;left:170px;top:59px;font-size:7px;line-height:1;white-space:nowrap;color:var(--ink);text-transform:uppercase}
.thanks-front .big{position:absolute;left:160px;top:80px;width:170px;text-align:center;font-family:"Open Sans",sans-serif;font-weight:300;color:#fff;font-size:48px;line-height:.95}

/* Thank-you back */
.thanks-back{left:32px;top:398px;width:368px;height:250px;background:var(--paper-soft);border:2px solid #2a2a2a}
.thanks-back .motto{position:absolute;left:26px;top:38px;width:190px;font-weight:700;font-size:9.5px;line-height:1.4;text-align:center;white-space:nowrap;color:var(--ink)}
.thanks-back .raised{position:absolute;left:68px;top:70px;font-size:9px;color:var(--ink)}
.thanks-back .note{position:absolute;left:26px;top:163px;font-size:7.5px;line-height:1.45;color:var(--ink-soft);width:220px}
.thanks-back .savanna{position:absolute;left:0;bottom:0;width:100%;height:52px;background:linear-gradient(180deg,rgba(200,206,200,0),#c7cdc6)}
.thanks-back .sponsors{position:absolute;left:26px;bottom:22px;gap:12px}

/* Poster */
.poster{left:428px;top:122px;width:342px;height:354px}
.poster .title{position:absolute;left:0;top:14px;width:100%;text-align:center;font-size:36px}
.poster .sub{position:absolute;left:0;top:54px;width:100%;text-align:center;font-size:23px}
.poster .tag{position:absolute;left:0;top:83px;width:100%;text-align:center;font-family:"Oswald",sans-serif;font-size:12px;color:#fff;text-transform:uppercase}
.poster .details{position:absolute;left:20px;top:247px;width:180px;text-align:center;font-weight:700;font-size:10.5px;line-height:1.25;color:#fff}
.poster-about{left:428px;top:478px;width:342px;height:58px;background:var(--board)}
.poster-about .photo{position:absolute;left:9px;top:3px;width:54px;height:52px;background:linear-gradient(135deg,#d9a678,#7a4a2e);border-radius:2px}
.poster-about p{position:absolute;left:72px;top:4px;width:268px;font-size:7px;line-height:1.3;color:#ddd}
.poster-about .benefit{position:absolute;left:72px;top:42px;font-size:7px;color:var(--brand)}
.poster-sponsors{left:428px;top:540px;width:342px;height:32px;background:var(--paper);justify-content:space-around;align-items:center}
.poster-band{left:428px;top:573px;width:342px;height:35px;background:var(--brand)}
.poster-band .name{position:absolute;left:6px;top:3px;font-family:"Oswald",sans-serif;font-weight:700;font-size:17px;line-height:1.1;color:#fff}
.poster-band .mission{position:absolute;left:6px;top:24px;font-size:6px;font-weight:700;color:#fff}
.poster-band .blurb{position:absolute;left:206px;top:4px;width:132px;font-size:5px;line-height:1.3;color:#fff}

/* Invitation */
.invite{left:796px;top:83px;width:368px;height:244px;background:var(--paper)}
.invite .face{position:absolute;left:12px;top:12px;width:346px;height:221px}
.invite .web{position:absolute;left:182px;top:20px;font-size:7px;color:#fff;font-weight:700;white-space:nowrap}
.invite .big{position:absolute;left:172px;top:32px;width:150px;text-align:center;font-family:"Oswald",sans-serif;font-weight:600;color:#fff;font-size:25px;line-height:1.05;text-transform:uppercase}
.invite .name{position:absolute;left:168px;top:92px;font-size:17px}
.invite .gala{position:absolute;left:184px;top:113px;font-size:9px;letter-spacing:1px}
.invite .venue{position:absolute;left:170px;top:130px;align-items:center;gap:10px}
.invite .venue small{font-size:6px;line-height:1.4;color:var(--ink);text-transform:uppercase}
.invite .dinner{position:absolute;left:166px;top:167px;width:170px;font-size:7px;line-height:10px;color:#8b1010;font-weight:700;text-align:center;white-space:nowrap}
.invite .benefit{position:absolute;left:166px;top:189px;width:170px;text-align:center;font-size:7px;color:#fff;font-weight:700;white-space:nowrap}

/* Ticket */
.ticket{left:802px;top:358px;width:362px;height:126px;background:var(--paper)}
.ticket .thumb{position:absolute;left:8px;top:8px;width:98px;height:110px}
.ticket .name{position:absolute;left:134px;top:26px;font-size:14px;font-weight:600}
.ticket .gala{position:absolute;left:138px;top:43px;font-size:8px;letter-spacing:1px;font-weight:600}
.ticket .info{position:absolute;left:134px;top:58px;font-size:6.5px;line-height:1.45;color:var(--ink-soft);text-transform:uppercase}
.ticket .host{position:absolute;left:230px;top:72px}
.ticket .rule{position:absolute;left:305px;top:14px;width:2px;height:98px;background:var(--ink)}
.ticket .price{position:absolute;left:310px;top:56px;width:48px;text-align:center;transform:rotate(-90deg);font-family:"Oswald",sans-serif;font-size:18px;color:var(--ink)}

/* Logo card */
.identity{left:802px;top:516px;width:362px;height:128px;background:var(--paper)}
.identity .name{position:absolute;left:0;top:24px;width:100%;text-align:center;font-weight:700;font-size:24px;color:var(--brand)}
.identity .mission{position:absolute;left:0;top:52px;width:100%;text-align:center;font-weight:700;font-size:8px;color:var(--ribbon)}
.identity .tag{position:absolute;left:0;top:69px;width:100%;text-align:center;font-size:9px;letter-spacing:2.3px;color:#b8161c}
.identity .sponsors{position:absolute;left:0;top:90px;width:100%;justify-content:center;gap:16px}

.sponsors{display:flex;position:absolute}
.sponsor{font-family:"Arimo",sans-serif;font-size:9px;color:var(--sponsor);white-space:nowrap}
.sponsors.tiny .sponsor{font-size:6px}
.sponsor.lead{font-size:11px}
</style>
</head>
<body>
<main class="board">

  <section class="piece thanks-front" aria-label="Thank you postcard front">
    <div class="face sunset">
      <div class="artwork" role="img" aria-label="Map of Africa with a layered heart, birds and giraffe at sunset" style="left:18px;top:18px;width:140px;height:200px"></div>
      <h2 class="headline title">Baobab Evening</h2>
      <p class="headline sub">2014 Fund Raising Gala</p>
      <span class="ribbon-mark" role="img" aria-label="Red awareness ribbon" style="left:160px;top:57px;width:7px;height:13px"></span>
      <p class="tag">Your Generosity. Our Passion. Saving Lives.</p>
      <p class="big">THANK YOU!</p>
    </div>
  </section>

  <section class="piece thanks-back" aria-label="Thank you postcard back">
    <p class="motto">YOUR GENEROSITY. OUR PASSION.<br>SAVING LIVES</p>
    <p class="raised">We raised over</p>
    <p class="note">Thank you for helping us break records this year!<br>Your contribution is an important part of our efforts<br>to help HIV affected children.<br><br>Thank You!</p>
    <div class="savanna" role="img" aria-label="Faint savanna and giraffe silhouette"></div>
    <div class="sponsors tiny">
      <span class="sponsor">Calder Ridge</span>
      <span class="sponsor">Northvale</span>
      <span class="sponsor">Kestrel Group</span>
      <span class="sponsor">Harborline Air</span>
    </div>
  </section>

  <section class="piece poster sunset" aria-label="Gala poster">
    <h1 class="headline title">Baobab Evening</h1>
    <p class="headline sub">2014 Fund Raising Gala</p>
    <p class="tag">Your Generosity. Our Passion. Saving Lives</p>
    <span class="ribbon-mark" role="img" aria-label="Red awareness ribbon" style="left:14px;top:80px;width:9px;height:26px"></span>
    <span class="ribbon-mark" role="img" aria-label="Red awareness ribbon" style="left:318px;top:80px;width:9px;height:26px"></span>
    <div class="artwork" role="img" aria-label="Map of Africa with a layered heart, birds and giraffe at sunset" style="left:88px;top:110px;width:190px;height:240px"></div>
    <p class="details">Saturday, October 18th, 2014<br>6:30pm – Calder Ridge Winery<br>$120 per person<br>Sit down dinner, wine and<br>entertainment included<br>Semi-formal</p>
  </section>
  <section class="piece poster-about" aria-label="Event description">
    <div class="photo" role="img" aria-label="Photograph of two children holding a hope sign"></div>
    <p>Come join us at Seattle's premier wine destination, Calder Ridge, and enjoy the region's best wines and an evening filled with the heart and spirit of Africa. Featuring formal sit down dinner, wine, African entertainment, heartwarming stories and auction.</p>
    <p class="benefit">All to benefit HIV affected children in Africa</p>
  </section>
  <section class="piece sponsors poster-sponsors" aria-label="Sponsors">
    <span class="sponsor lead">Calder Ridge</span>
    <span class="sponsor lead">Northvale</span>
    <span class="sponsor lead">Kestrel Group</span>
    <span class="sponsor lead">Harborline Air</span>
  </section>
  <section class="piece poster-band" aria-label="Organisation band">
    <p class="name">LANTERNS &amp; LINDEN</p>
    <p class="mission">HELPING HIV POSITIVE ORPHANS IN AFRICA</p>
    <p class="blurb">Lanterns &amp; Linden is a 501(c)(3) based in Seattle which focuses on providing life-prolonging medication and support to children in Africa who have been affected by HIV/AIDS.</p>
  </section>

  <section class="piece invite" aria-label="Save the date postcard">
    <div class="face sunset">
      <div class="artwork" role="img" aria-label="Map of Africa with a layered heart, birds and giraffe at sunset" style="left:20px;top:14px;width:140px;height:200px"></div>
      <p class="web">visit our web site to get your tickets</p>
      <p class="big">You are<br>invited!</p>
      <p class="headline name">LANTERNS &amp; LINDEN</p>
      <p class="headline gala">2014 Fundraising Gala</p>
      <div class="sponsors venue">
        <span class="sponsor lead" style="color:var(--ink)">Calder Ridge</span>
        <small>October 18th,<br>Calder Ridge Winery</small>
      </div>
      <p class="dinner">Sit down dinner, wine and entertainment<br>Semi - formal</p>
      <p class="benefit">All to benefit HIV affected children in Africa</p>
    </div>
  </section>

  <section class="piece ticket" aria-label="Ticket">
    <div class="thumb sunset" role="img" aria-label="Map of Africa with a layered heart at sunset">
      <div class="artwork" style="left:14px;top:10px;width:70px;height:92px"></div>
    </div>
    <p class="headline name">LANTERNS &amp; LINDEN</p>
    <p class="headline gala">2014 Fundraising Gala</p>
    <p class="info">Saturday<br>October 18th,<br>6:30PM – Semi-formal<br>Calder Ridge Winery</p>
    <span class="sponsor host">Calder Ridge</span>
    <span class="rule"></span>
    <p class="price">$120</p>
  </section>

  <section class="piece identity" aria-label="Organisation identity card">
    <p class="name">LANTERNS &amp; LINDEN</p>
    <p class="mission">HELPING HIV POSITIVE ORPHANS IN AFRICA</p>
    <p class="tag">Your Generosity. Our Passion. Saving Lives.</p>
    <div class="sponsors">
      <span class="sponsor">Calder Ridge</span>
      <span class="sponsor">Northvale</span>
      <span class="sponsor">Kestrel Group</span>
      <span class="sponsor">Harborline Air</span>
    </div>
  </section>

</main>
</body>
</html>
```